Silver Heron Motor Works needs a logo design

I'm after a logo design for a new Female owned automotive repair workshop in the Queanbeyan/Canberra Australia Area.
We offer repairs on all passenger cars, 4wds and light trucks emphasising a strong honest work ethic and a genuine interest in the customer and their vehicles needs. With business details on the front of the card and what we offer on the back.
I would like a design with a phoenix in multiple colours maybe hovering over a flaming wheel or a car with wheels flaming with the phoenix hovering up out of the flames
Target Market(s)
All Vehicle users
Industry/Entity Type
Automotive
Contact Information for Business Card
On the front
Silver Heron Motor
Marla Pettigrew Owner/ Mechanic 0471385026
email marla@silverheronmotor.com.au
Website www.silverheronmotorworks.com.au
On the back
All Cars, 4WDs, Light trucks, makes and models
Log book servicing
General vehicle servicing
Major vehicle servicing
brake and clutch servicing and repairs
Suspension repairs
cooling systems
All major and minor mechanical repairs
minor electrical rewiring and repairs
Colors
Designer to choose colors to be used in the design.
Look and feel

```html
<!DOCTYPE html>
<html lang="en">
<head>
<meta charset="utf-8">
<title>Silver Heron Motor – Business Card</title>
<link rel="stylesheet" href="https://fonts.googleapis.com/css2?family=Montserrat:wght@400;500&family=Saira+Condensed:wght@600&display=swap">
<style>
  :root {
    --backdrop: #d9d9d7;
    --card-dark: #1b1b1d;
    --card-mid: #2c2c2f;
    --accent-orange: #f07a1c;
    --accent-red: #e2461b;
    --text-light: #f2f2f2;
    --phoenix-green: #2f9a6b;
    --phoenix-teal: #2a7f8c;
    --flame-amber: #f5a12a;
  }
  * { box-sizing: border-box; margin: 0; padding: 0; }
  html, body {
    width: 1200px; height: 1200px; overflow: hidden;
    background: var(--backdrop);
  }
  .sheet {
    width: 1200px; height: 1200px;
    display: flex; flex-direction: column; align-items: center; justify-content: center;
    gap: 56px;
  }
  .card {
    position: relative;
    width: 920px; height: 526px;
    border-radius: 34px;
    overflow: hidden;
    background: radial-gradient(ellipse at 60% 40%, var(--card-mid) 0%, var(--card-dark) 75%);
    box-shadow: 0 6px 18px rgba(0,0,0,0.25);
  }

  /* Front */
  .brand-name {
    position: absolute; top: 56px; right: 60px;
    font-family: "Montserrat", sans-serif; font-weight: 500;
    font-size: 54px; color: var(--accent-orange);
    letter-spacing: 1px;
  }
  .phoenix-art {
    position: absolute; right: 40px; bottom: 34px;
    width: 400px; height: 290px; border-radius: 40% 50% 30% 45%;
    background: linear-gradient(160deg, var(--phoenix-green) 0%, var(--phoenix-teal) 35%, var(--flame-amber) 70%, var(--accent-red) 100%);
    opacity: 0.9;
  }
  .contact {
    position: absolute; left: 56px; bottom: 64px;
    font-family: "Montserrat", sans-serif; color: var(--text-light);
  }
  .contact-name {
    font-size: 36px; font-weight: 400; color: var(--accent-orange);
    text-transform: uppercase; letter-spacing: 1.5px; line-height: 1.1;
  }
  .contact-role {
    font-size: 28px; text-transform: uppercase; letter-spacing: 1.5px; margin-bottom: 8px;
  }
  .contact-line {
    display: flex; align-items: center; gap: 10px;
    font-size: 22px; line-height: 1.45;
  }
  .contact-icon { width: 22px; height: 22px; flex: none; }

  /* Back */
  .services {
    position: absolute; z-index: 2;
    list-style: none;
    font-family: "Saira Condensed", sans-serif; font-weight: 600;
    color: var(--accent-orange); text-transform: uppercase;
    font-size: 30px; line-height: 36px; transform: skewX(-8deg);
  }
  .services--left { top: 36px; left: 60px; }
  .services--right { top: 128px; right: 60px; text-align: right; }
  .car-art {
    position: absolute; z-index: 1; left: 30px; bottom: 22px;
    width: 560px; height: 150px; border-radius: 46% 60% 20% 30%;
    background: linear-gradient(90deg, var(--flame-amber) 0%, var(--accent-orange) 45%, var(--accent-red) 100%);
    opacity: 0.9;
  }
</style>
</head>
<body>
<main class="sheet">

  <section class="card card--front">
    <div class="brand-name">Silver Heron Motor</div>
    <div class="phoenix-art" role="img" aria-label="Multicoloured phoenix rising out of flames"></div>
    <div class="contact">
      <p class="contact-name">Marla Pettigrew</p>
      <p class="contact-role">Owner/ Mechanic</p>
      <p class="contact-line">
        <svg class="contact-icon" viewBox="0 0 24 24" aria-hidden="true">
          <circle cx="12" cy="12" r="12" fill="var(--accent-orange)"/>
          <path d="M8 6.5l2 0 1 3-1.5 1a7 7 0 0 0 4 4l1-1.5 3 1 0 2a1.5 1.5 0 0 1-1.5 1.5A10 10 0 0 1 6.5 8 1.5 1.5 0 0 1 8 6.5z" fill="var(--card-dark)"/>
        </svg>
        0471385026
      </p>
      <p class="contact-line">
        <svg class="contact-icon" viewBox="0 0 24 24" aria-hidden="true">
          <circle cx="12" cy="12" r="12" fill="var(--accent-orange)"/>
          <rect x="6" y="8" width="12" height="8.5" rx="1" fill="var(--card-dark)"/>
          <path d="M6.5 8.5l5.5 4.5 5.5-4.5" stroke="var(--accent-orange)" stroke-width="1.3" fill="none"/>
        </svg>
        marla@silverheronmotor.com.au
      </p>
    </div>
  </section>

  <section class="card card--back">
    <ul class="services services--left">
      <li>All cars, 4WDs, light trucks,</li>
      <li>makes and models</li>
      <li>Log book servicing</li>
      <li>General vehicle servicing</li>
      <li>Major vehicle servicing</li>
    </ul>
    <ul class="services services--right">
      <li>Brake and clutch servicing</li>
      <li>and repairs</li>
      <li>Suspension repairs</li>
      <li>Cooling systems</li>
      <li>All major and minor mechanical repairs</li>
      <li>Minor electrical rewiring and repairs</li>
    </ul>
    <div class="car-art" role="img" aria-label="Orange sports car with flaming wheels"></div>
  </section>

</main>
</body>
</html>
```